Bramwell Dental personal information forms

We are a Dental Practice that require an update to our information forms, there are 3 versions of it.
I will attach our old ones, we need to keep the same information on there, we just want them to look better and use our current logo and colours.
Our website is www.bramwelldental-example.net
Our facebook is www.facebook.com/bramwelldentalkestonwalk/
..................................................................................................

Target Market(s)

Everyone, easy to read

Industry/Entity Type

Dental Clinic

Colors
0692cd
34a6d7
cee9f5
ffffff
0255a3
3276b5

Requirements
Must have
• Logo
• Our colours
• same information as the uploaded versions
Should not have
• any other colour besides the blues, black and white

```html
<!DOCTYPE html>
<html lang="en">
<head>
<meta charset="utf-8">
<title>Bramwell Dental – Patient Information Forms</title>
<link href="https://fonts.googleapis.com/css2?family=Source+Sans+3:ital,wght@0,400;0,600;0,700;1,400;1,600;1,700&display=swap" rel="stylesheet">
<style>
:root{
  --blue:#0692cd;
  --sky:#34a6d7;
  --pale:#cee9f5;
  --navy:#0255a3;
  --mid:#3276b5;
  --ink:#1a1a1a;
  --paper:#ffffff;
  --stage:#2e2e30;
}
*{box-sizing:border-box;margin:0;padding:0}
html,body{width:1200px;height:1200px;overflow:hidden;background:var(--stage)}
body{font-family:"Source Sans 3",Arial,sans-serif;color:var(--ink)}
.board{position:relative;width:1400px;height:1400px;transform:scale(.857143);transform-origin:0 0}
.page{position:absolute;width:415px;height:583px;background:var(--paper);padding:0 16px;font-size:6px;line-height:1.25;overflow:hidden}
.p1{left:222px;top:76px}.p2{left:805px;top:76px}.p3{left:235px;top:743px}.p4{left:832px;top:743px}

.masthead{position:relative;height:62px;display:flex;align-items:center;justify-content:center;margin:0 -16px}
.masthead::before,.masthead::after{content:"";position:absolute;top:32px;height:3px;background:var(--pale);width:30%}
.masthead::before{left:0}.masthead::after{right:0}
.brand{font-size:26px;font-weight:600;color:var(--blue);letter-spacing:.5px;padding-top:6px}

.intro-row{display:flex;justify-content:space-between;align-items:flex-start}
.doctors{font-style:italic;font-weight:700;color:var(--mid);font-size:8.5px}
.role{font-style:italic;font-weight:700;font-size:8.5px;margin-top:2px}
.sticker{width:138px;height:32px;border:1.2px solid var(--mid);font-style:italic;font-size:7.5px;display:flex;align-items:center;justify-content:center}
.welcome{color:var(--blue);font-weight:700;font-size:9.5px;margin:8px 0 4px}
.lead{font-size:6.3px}
.lead .hl{color:var(--blue)}

.q{display:flex;justify-content:space-between;align-items:flex-end;margin-top:9px;font-size:5.8px}
.q .yn{color:var(--blue);font-weight:700;font-size:7.5px;padding-right:6px;white-space:nowrap}
.field{background:var(--pale);height:19px;margin-top:3px}
.field.tall{height:21px}

.cond-lead{margin-top:10px;font-size:5.8px}
.checks{display:grid;grid-template-columns:repeat(3,1fr);margin-top:5px}
.checks ul{list-style:none;padding-left:4px;border-right:.6px solid #999}
.checks ul:last-child{border-right:0}
.checks li{display:flex;align-items:center;gap:6px;height:11px;font-size:6.3px}
.box{width:5px;height:5px;border:.8px solid var(--mid);flex:none}

.declare{font-weight:700;font-size:6.3px;margin-top:12px}
.consent{font-size:5.3px;margin-top:10px;color:#333}
.sign{display:flex;gap:8px;font-size:6.5px;margin-top:18px;align-items:flex-end}
.sign .line{border-bottom:.7px solid var(--ink);height:6px}

/* patient information grid */
.info{border:1px solid var(--sky);margin-top:7px;display:grid;grid-template-columns:58% 42%;font-size:4.8px}
.info h4{background:var(--pale);text-align:center;font-size:6.8px;font-weight:600;padding:1px 0}
.titles{display:flex;justify-content:space-around;color:var(--mid);font-size:6.5px;padding:2px 0;border-bottom:.5px solid var(--sky)}
.row{display:flex;border-bottom:.5px solid var(--sky);min-height:8px}
.row .k{width:34px;padding-left:2px;border-right:.5px solid var(--sky)}
.row .v{flex:1;display:flex;justify-content:flex-end}
.row .pc{width:48px;border-left:.5px solid var(--sky);padding-left:2px}
.left{border-right:1px solid var(--sky)}
.right .row .k{width:30px}
.methods{display:flex;justify-content:space-around;padding:0 2px}
.sub-h{background:var(--pale);text-align:center;font-size:6.5px;font-weight:600}

/* page 3 */
.other{border:1px solid var(--mid);margin-top:16px;padding:10px 6px 6px;position:relative}
.other-h{position:absolute;top:-6px;left:50%;transform:translateX(-50%);background:var(--paper);border-bottom:2px solid var(--pale);padding:0 16px;font-size:6.5px;font-weight:600}
.box-table{border:.6px solid var(--mid);margin-top:4px;font-size:5px}
.box-table .row{border-color:var(--mid);min-height:11px}
.box-table .row .k{width:30px;border-color:var(--mid)}
.account{background:var(--pale);font-size:5.4px;padding:2px 3px;font-family:Georgia,serif}
.options{display:flex;justify-content:space-between;padding:3px 6px;font-size:5px}
.note{font-style:italic;font-weight:600;font-size:5px;margin-top:7px}
.turn{position:absolute;right:28px;bottom:24px;color:var(--blue);font-weight:600;font-size:8px;display:flex;align-items:center;gap:3px}

/* page 4 */
.banner{background:var(--pale);font-size:5.4px;padding:3px 6px;margin-top:8px}
.sect{color:var(--blue);font-style:italic;font-weight:700;font-size:7.5px;margin-top:5px}
.frame{border:1px solid var(--mid);padding:2px 6px 4px}
.dental-checks{display:grid;grid-template-columns:repeat(3,1fr);font-size:5.4px}
.dental-checks li{list-style:none;display:flex;gap:5px;align-items:center;height:10px}
.scale{display:flex;justify-content:space-between;font-size:5px;margin-top:4px;padding-right:60px}
.scale span{display:flex;gap:4px;align-items:center}
.gp{border:.6px solid var(--mid);margin-top:2px;font-size:5px}
.gp .row{border-color:var(--mid);min-height:11px}
.gp .row .k{width:92px;text-align:right;padding-right:3px;border-color:var(--mid)}
.p4 .q{margin-top:6px;font-size:5.2px}
.p4 .q .yn{font-size:6.5px}
.p4 .field{height:14px}
.p4 .checks li{height:10px;font-size:5.4px}
</style>
</head>
<body>
<main class="board">

<!-- Form A: returning patient, short -->
<section class="page p1">
  <header class="masthead"><span class="brand">Bramwell Dental</span></header>
  <div class="intro-row">
    <div>
      <p class="doctors">Dr. Lewis Okafor &amp; Dr. Harriet Quill</p>
      <p class="role">Dental Surgeons</p>
    </div>
    <div class="sticker">Affix patient sticker here.</div>
  </div>
  <h2 class="welcome">Welcome back to our practice!</h2>
  <p class="lead"><span class="hl">THIS INFORMATION IS CONFIDENTIAL</span> and is necessary to enable us to offer you <span class="hl">THE BEST POSSIBLE CARE.</span><br>It is now mandatory to have a written updated medical history every 2 years and we would appreciate your time in thoroughly completing this form.</p>
  <div class="q"><span>Are you currently or have you taken any prescribed medication or dietary supplements in the last 12 months?.<br>(If YES, please list below)</span><span class="yn">YES/NO</span></div>
  <div class="field"></div>
  <div class="q"><span>Allergies / Reactions? If YES, please list below</span><span class="yn">YES/NO</span></div>
  <div class="field"></div>
  <p class="cond-lead">Have you ever had or are you suffering from any of the following? Please tick any that apply:</p>
  <div class="checks">
    <ul><li><i class="box"></i>Rheumatic fever</li><li><i class="box"></i>Epilepsy</li><li><i class="box"></i>Asthma</li><li><i class="box"></i>Tuberculosis</li><li><i class="box"></i>Radiation Therapy</li><li><i class="box"></i>Dizziness, fainting</li><li><i class="box"></i>Hepatitis A B or C</li><li><i class="box"></i>Recent eye surgery</li></ul>
    <ul><li></li><li><i class="box"></i>Diabetes</li><li><i class="box"></i>Kidney Disease</li><li><i class="box"></i>Heart Attack</li><li><i class="box"></i>High Blood Pressure</li><li><i class="box"></i>Bleeding problems</li><li><i class="box"></i>Artificial joints</li><li><i class="box"></i>Respiratory problems</li></ul>
    <ul><li></li><li><i class="box"></i>HIV Positive</li><li><i class="box"></i>High cholesterol</li><li><i class="box"></i>Cancer</li><li><i class="box"></i>Pace-maker</li><li><i class="box"></i>Osteoporosis</li><li><i class="box"></i>Heart rate problems</li><li><i class="box"></i>Heart murmur</li></ul>
  </div>
  <div class="q"><span>Do you have any disease, condition or problem not listed above?</span><span class="yn">YES/NO</span></div>
  <div class="field"></div>
  <div class="q"><span>Have you had surgery or been to hospital in the last 5 years?(If YES, please give details)</span><span class="yn">YES/NO</span></div>
  <div class="field"></div>
  <div class="q"><span>For Women: Are you pregnant?If yes, how many months?</span><span class="yn">YES/NO</span></div>
  <div class="field"></div>
  <div class="q"><span>Do you currently or have you ever smoked?</span><span class="yn">YES/NO</span></div>
  <div class="field"></div>
  <p class="declare">The information that I have provided is to the best of my knowledge true and correct and I understand that it is my responsibility to of any changes in my medical status.</p>
  <div class="sign"><span>Patient/Parent/Person Responsible Signature:</span><span class="line" style="width:118px"></span><span style="margin-left:24px">Date:</span><span class="line" style="width:66px"></span></div>
</section>

<!-- Form B: returning patient, full details -->
<section class="page p2">
  <header class="masthead"><span class="brand">Bramwell Dental</span></header>
  <p class="doctors" style="margin-top:-8px">Dr. Harriet Quill &amp; Dr. Lewis Okafor</p>
  <p class="role">Dental Surgeons</p>
  <h2 class="welcome" style="font-size:8px;margin:4px 0 2px">Welcome back to our practice!</h2>
  <p class="lead" style="font-size:5px"><span class="hl">THIS INFORMATION IS CONFIDENTIAL</span> and is necessary to enable us to offer you <span class="hl">THE BEST POSSIBLE CARE.</span> Because we haven't seen you in some time and because we care about your health status, please take you time and thoroughly complete the following update of your personal and medical information. It is essential that we know about your past and present medical history. Many medical conditions may interfere with dental procedures.</p>
  <div class="info">
    <div class="left">
      <h4>PATIENT INFORMATION</h4>
      <div class="titles"><span>Mrs</span><span>Miss</span><span>Mr</span><span>Master</span><span>Dr</span><span>Other</span></div>
      <div class="row"><span class="k">Surname</span><span class="v"></span></div>
      <div class="row"><span class="k">First Name</span><span class="v"></span></div>
      <div class="row"><span class="k">Preferred</span><span class="v"></span></div>
      <div class="row"><span class="k">Date of Birth</span><span class="v"></span></div>
      <div class="row" style="min-height:22px"><span class="k">Current Residential Address</span><span class="v" style="align-items:flex-end"><span class="pc">Postcode:</span></span></div>
      <div class="row" style="min-height:24px"><span class="k">Postal Residential Address (if different)</span><span class="v" style="align-items:flex-end"><span class="pc">Postcode:</span></span></div>
      <div class="row"><span class="k">Occupation</span><span class="v"></span></div>
      <div class="row" style="border-bottom:0"><span class="k">Employer</span><span class="v"></span></div>
    </div>
    <div class="right">
      <h4>PATIENT CONTACT INFORMATION</h4>
      <div class="row" style="min-height:22px"><span class="k">Phone</span><span class="v" style="flex-direction:column;justify-content:space-around"><span>M:</span><span>H:</span><span>W:</span></span></div>
      <div class="row"><span class="k">Email</span></div>
      <div class="row"><span class="k">Preferred</span></div>
      <div>Preferred method of communication:</div>
      <div class="methods row"><span>SMS</span><span>Phone</span><span>Email</span><span>Mail</span></div>
      <div class="row" style="min-height:11px"><span>Referred by:</span></div>
      <div class="sub-h">EMERGENCY CONTACT</div>
      <div class="row"><span class="k">Name</span></div>
      <div class="row"><span class="k">Relationship</span></div>
      <div class="row" style="border-bottom:0"><span class="k">Contact number</span></div>
    </div>
  </div>
  <div class="q" style="margin-top:4px;font-size:5px"><span>Are you currently or have you taken any prescribed medication or dietary supplements<br>in the last 12 months?. (If YES, please list below)</span><span class="yn" style="font-size:6.5px">YES/NO</span></div>
  <div class="field"></div>
  <div class="q" style="font-size:5px"><span>Allergies / Reactions? If YES, please list below</span><span class="yn" style="font-size:6.5px">YES/NO</span></div>
  <div class="field"></div>
  <p class="cond-lead" style="font-size:5px;margin-top:7px">Have you ever had or are you suffering from any of the following? Please tick any that apply:</p>
  <div class="checks" style="margin-top:2px">
    <ul><li><i class="box"></i>Rheumatic fever</li><li><i class="box"></i>Epilepsy</li><li><i class="box"></i>Asthma</li><li><i class="box"></i>Tuberculosis</li><li><i class="box"></i>Radiation Therapy</li><li><i class="box"></i>Dizziness, fainting</li><li><i class="box"></i>Hepatitis A B or C</li></ul>
    <ul><li><i class="box"></i>Recent eye surgery</li><li><i class="box"></i>Diabetes</li><li><i class="box"></i>Kidney Disease</li><li><i class="box"></i>Heart Attack</li><li><i class="box"></i>High Blood Pressure</li><li><i class="box"></i>Bleeding problems</li><li><i class="box"></i>Artificial joints</li></ul>
    <ul><li><i class="box"></i>Respiratory problems</li><li><i class="box"></i>HIV Positive</li><li><i class="box"></i>High cholesterol</li><li><i class="box"></i>Cancer</li><li><i class="box"></i>Pace-maker</li><li><i class="box"></i>Osteoporosis</li><li><i class="box"></i>Heart rate problems</li><li><i class="box"></i>Heart murmur</li></ul>
  </div>
  <div class="q" style="margin-top:-6px;font-size:5px"><span>Do you have any disease, condition or problem not listed above?</span><span class="yn" style="font-size:6.5px">YES/NO</span></div>
  <div class="field"></div>
  <div class="q" style="font-size:5px"><span>Have you had surgery or been to hospital in the last 5 years?(If YES, please give details)</span><span class="yn" style="font-size:6.5px">YES/NO</span></div>
  <div class="field"></div>
  <div class="q" style="font-size:5px"><span>For Women: Are you pregnant?If yes, how many months?</span><span class="yn" style="font-size:6.5px">YES/NO</span></div>
  <div class="field"></div>
  <p class="consent">The information that I have provided is to the best of my knowledge true and correct and I understand that it is my responsibility to inform of any changes in my medical status. This is to certify that I, the undersigned, consent to the performing of the dental and oral surgery procedures agreed to be necessary or advisable, including the use of local anaesthetic as indicated and I will assume responsibility for the fees associated with these procedures. Therefore, I shall pay any legal costs, including solicitor and own costs, tracing costs and any collection commission incurred by Bramwell Dental as a result of my failure to pay any amount due to Bramwell Dental.</p>
  <div class="sign" style="margin-top:10px"><span>Patient/Parent/Person Responsible Signature:</span><span class="line" style="width:122px"></span><span style="margin-left:22px">Date:</span><span class="line" style="width:66px"></span></div>
</section>

<!-- Form C: new patient, side one -->
<section class="page p3">
  <header class="masthead"><span class="brand">Bramwell Dental</span></header>
  <p class="doctors" style="margin-top:-4px">Dr. Harriet Quill &amp; Dr. Lewis Okafor</p>
  <p class="role">Dental Surgeons</p>
  <h2 class="welcome" style="font-size:8px;margin:6px 0 3px">Welcome to our practice!</h2>
  <p class="lead" style="font-size:5.3px"><span class="hl">THIS INFORMATION IS CONFIDENTIAL</span> and is necessary to enable us to offer you <span class="hl">THE BEST POSSIBLE CARE.</span> At Bramwell Dental, we respect and protect the privacy of our patients and as such will only ask for information relevant to the treatment we may need to provide you. Thank you!</p>
  <div class="info">
    <div class="left">
      <h4>PATIENT INFORMATION</h4>
      <div class="titles"><span>Mrs</span><span>Miss</span><span>Mr</span><span>Master</span><span>Dr</span><span>Other</span></div>
      <div class="row"><span class="k">Surname</span><span class="v"></span></div>
      <div class="row"><span class="k">First Name</span><span class="v"></span></div>
      <div class="row"><span class="k">Preferred</span><span class="v"></span></div>
      <div class="row"><span class="k">Date of Birth</span><span class="v"></span></div>
      <div class="row" style="min-height:22px"><span class="k">Current Residential Address</span><span class="v" style="align-items:flex-end"><span class="pc">Postcode:</span></span></div>
      <div class="row" style="min-height:26px"><span class="k">Postal Residential Address (if different)</span><span class="v" style="align-items:flex-end"><span class="pc">Postcode:</span></span></div>
      <div class="row"><span class="k">Occupation</span><span class="v"></span></div>
      <div class="row" style="border-bottom:0"><span class="k">Employer</span><span class="v"></span></div>
    </div>
    <div class="right">
      <h4>PATIENT CONTACT INFORMATION</h4>
      <div class="row" style="min-height:24px"><span class="k">Phone</span><span class="v" style="flex-direction:column;justify-content:space-around"><span>M:</span><span>H:</span><span>W:</span></span></div>
      <div class="row"><span class="k">Email</span></div>
      <div class="row"><span class="k">Preferred</span></div>
      <div>Preferred method of communication:</div>
      <div class="methods row"><span>SMS</span><span>Phone</span><span>Email</span><span>Mail</span></div>
      <div class="row" style="min-height:14px"><span>Referred by:</span></div>
      <div class="sub-h">EMERGENCY CONTACT</div>
      <div class="row"><span class="k">Name</span></div>
      <div class="row"><span class="k">Relationship</span></div>
      <div class="row" style="border-bottom:0"><span class="k">Contact number</span></div>
    </div>
  </div>
  <div class="other">
    <span class="other-h">OTHER INFORMATION</span>
    <p class="account" style="margin-top:10px">Person responsible for your account (if yourself, please tick this box)</p>
    <div class="box-table" style="border-top:0">
      <div class="row"><span class="k">Name</span></div>
      <div class="row"><span class="k">Phone</span></div>
      <div class="row" style="min-height:24px;border-bottom:0"><span class="k">Address</span><span class="v" style="align-items:flex-end"><span class="pc" style="border-color:var(--mid)">Postcode:</span></span></div>
    </div>
    <div class="q" style="margin-top:16px;font-size:5.4px"><span>Do you have Private Health Insurance?</span><span class="yn" style="font-size:6.5px">YES/NO</span></div>
    <p style="font-size:5.4px;margin-top:5px">If YES, please specify the name (e.g. Northgate Health)</p>
    <div class="box-table">
      <div class="row"><span class="k">Name</span></div>
      <div class="row" style="border-bottom:0"><span class="k" style="width:48px">Patient number</span></div>
    </div>
    <div class="q" style="margin-top:10px;font-size:5.4px"><span>Do you have Private Health Insurance?</span><span class="yn" style="font-size:6.5px">YES/NO</span></div>
    <div class="box-table">
      <p style="padding:2px 3px">If yes, please circle one of the following options:</p>
      <div class="options"><span>CDBS</span><span>DVA</span><span>Workcover</span><span>MAC</span><span style="width:60px">Other:</span></div>
    </div>
    <p class="note">Please note: if you are claiming please ensure that you have the relevant letters and/or forms as payment is required at time of treatment.</p>
    <div class="box-table">
      <p style="padding:2px 3px;border-bottom:.6px solid var(--mid)">How did you hear about us? (Please circle one option below)</p>
      <div class="options" style="border-bottom:.6px solid var(--mid)"><span>Referred</span><span>Local Directory</span><span>Advertisement</span><span>Internet</span><span style="width:50px">Other:</span></div>
      <p style="padding:2px 3px">If referred, please provide name of referrer:</p>
      <p style="padding:2px 3px 6px">Relationship to you:</p>
    </div>
  </div>
  <div class="turn">Please turn over
    <svg width="14" height="6" viewBox="0 0 14 6"><path d="M0 3H12M9 0.5L12.5 3L9 5.5" stroke="#0692cd" stroke-width="1" fill="none"/></svg>
  </div>
</section>

<!-- Form C: new patient, side two -->
<section class="page p4">
  <p class="banner">It is essential that we know about your past and present medical history. Many medical conditions may interfere with dental procedures.<br>Please take your time and thoroughly complete the following section.</p>
  <h3 class="sect">DENTAL HISTORY</h3>
  <div class="frame">
    <p style="font-size:5.2px">Are you concerned about or experiencing any of the following dental problems? (Please tick as many as applies)</p>
    <ul class="dental-checks">
      <li><i class="box"></i>Sensitivity to hot and cold</li><li><i class="box"></i>Food trapping between teeth</li><li><i class="box"></i>Clicking/pain in the jaw joints</li>
      <li><i class="box"></i>Staining of your teeth</li><li><i class="box"></i>Discoloured fillings</li><li><i class="box"></i>Roughness of existing fillings</li>
      <li><i class="box"></i>Bleeding Gums</li><li><i class="box"></i>Bad breath</li><li><i class="box"></i>Tenderness when eating</li>
      <li><i class="box"></i>Crowding of teeth</li><li><i class="box"></i>Grinding/Clenching of your teeth</li><li><i class="box"></i>Poorly fitted crowns/dentures</li>
    </ul>
    <div class="q" style="margin-top:3px;font-size:5.2px"><span>What is the main purpose of your visit today?</span></div>
    <div class="field" style="height:14px"></div>
    <div class="q" style="margin-top:5px;font-size:5.2px"><span>How long has it been since your last dental visit?</span></div>
    <div class="field" style="height:14px"></div>
    <div class="q" style="margin-top:5px;font-size:5.2px"><span>Does dental treatment make you nervous?</span></div>
    <div class="scale"><span><i class="box"></i>No</span><span><i class="box"></i>Slightly</span><span><i class="box"></i>Moderately</span><span><i class="box"></i>Extremely</span></div>
  </div>
  <h3 class="sect">MEDICAL HISTORY</h3>
  <div class="gp">
    <div class="row"><span class="k" style="text-align:left;padding-left:3px">Name of your Family Doctor (GP)</span></div>
    <div class="row"><span class="k">Clinic</span></div>
    <div class="row" style="border-bottom:0"><span class="k">Phone</span></div>
  </div>
  <div class="q"><span>Have you taken any prescribed medication or dietary supplements in the last 12 months? (If YES, please list below)</span><span class="yn">YES/NO</span></div>
  <div class="field"></div>
  <div class="q"><span>Allergies / Reactions? If yes, please list below:</span><span class="yn">YES/NO</span></div>
  <div class="field"></div>
  <div class="q"><span>Has anybody in your family history ever suffered from heart problems? (Please give details below)</span><span class="yn">YES/NO</span></div>
  <div class="field"></div>
  <p class="cond-lead" style="font-size:5.2px;margin-top:6px">Have you ever had or are you suffering from any of the following? Please tick any that apply:</p>
  <div class="checks" style="margin-top:2px">
    <ul><li><i class="box"></i>Rheumatic fever</li><li><i class="box"></i>Epilepsy</li><li><i class="box"></i>Asthma</li><li><i class="box"></i>Tuberculosis</li><li><i class="box"></i>Radiation Therapy</li><li><i class="box"></i>Dizziness, fainting</li><li><i class="box"></i>Hepatitis A B or C</li></ul>
    <ul><li><i class="box"></i>Diabetes</li><li><i class="box"></i>Kidney Disease</li><li><i class="box"></i>Heart Attack</li><li><i class="box"></i>High Blood Pressure</li><li><i class="box"></i>Bleeding problems</li><li><i class="box"></i>Artificial joints</li><li><i class="box"></i>Respiratory problems</li></ul>
    <ul><li><i class="box"></i>HIV Positive</li><li><i class="box"></i>High cholesterol</li><li><i class="box"></i>Cancer</li><li><i class="box"></i>Pace-maker</li><li><i class="box"></i>Osteoporosis</li><li><i class="box"></i>Heart rate problems</li><li><i class="box"></i>Heart murmur</li></ul>
  </div>
  <div class="q"><span>Have you taken any prescribed medication or dietary supplements in the last 12 months? (If YES, please list below)</span><span class="yn">YES/NO</span></div>
  <div class="field"></div>
  <div class="q"><span>Allergies / Reactions? If yes, please list below:</span><span class="yn">YES/NO</span></div>
  <div class="field"></div>
  <div class="q"><span>Has anybody in your family history ever suffered from heart problems? (Please give details below)</span><span class="yn">YES/NO</span></div>
  <div class="field"></div>
  <p class="consent" style="margin-top:8px"><b><i>The information that I have provided is to the best of my knowledge true and correct and I understand that it is my responsibility to inform of any changes in my medical status.</i></b><br>This is to certify that I, the undersigned, consent to the performing of the dental and oral surgery procedures agreed to be necessary or advisable, including the use of local anaesthetic as indicated and I will assume responsibility for the fees associated with these procedures. Therefore, I shall pay any legal costs, including solicitor and own costs, tracing costs and any collection commission incurred by Bramwell Dental as a result of my failure to pay any amount due to Bramwell Dental.</p>
  <div class="sign" style="margin-top:10px"><span>Patient/Parent/Person Responsible Signature:</span><span class="line" style="width:122px"></span><span style="margin-left:22px">Date:</span><span class="line" style="width:62px"></span></div>
</section>

</main>
</body>
</html>
```